Marlowick Investment Partners Website | ||
Financial Services | ||
mipfundexample.com | ||
The company is an investment fund. The site must inspire trust and confidence yet have style. It must be VERY professional. | ||
I like things simple and elegant. Rich and classy in appearance. I don't care too much about colors, but it's probably easiest to use the colors already used in my logos. | ||
Clean/Simple Professional Content Driven Conservative Sophisticated Corporate Modern Elegant Traditional Masculine |
left side | ||
https://www.castrelfunds.example/cm/Satellite?pagename=cfVanityWrapper&UserFriendlyURL=home | ||
http://www.tuvrelle.example/ | ||
http://www2.pinegate.example/US/individual-investors | ||
The site doesn't need to be terribly complex nor work as a stand-alone source for sales. It is mainly a source for further information for people I have talked to about the fund personally. It should also be a place for current clients to check on performance of their portfolios. Of the websites listed above: I like Castrel Banks's appearance I like Tuvrelle's layout and simplicity pinegate I like in general I also made a mock up of how i saw the site, which I'll upload once the contest is up and running. |

```html
<!DOCTYPE html>
<html lang="en">
<head>
<meta charset="utf-8">
<title>Marlowick Investment Partners — Client Access</title>
<link rel="stylesheet" href="https://fonts.googleapis.com/css2?family=Open+Sans:wght@400;600;700&display=swap">
<style>
  :root {
    --page-bg: #f2f1ef;
    --card-bg: #ffffff;
    --stage-bg: #ccc6bb;
    --stage-shape: #c3bcb0;
    --band-bg: #b7af a1;
    --band: #b6ae a0;
    --band-tone: #b6aea0;
    --band-line: #cdc7bc;
    --logo-panel: #0b0b0c;
    --accent: #1b8fb3;
    --accent-dark: #146f8c;
    --ink: #2c2c2c;
    --ink-soft: #5a5650;
    --field: #f4f3f0;
    --button: #4a4844;
  }
  * { box-sizing: border-box; margin: 0; padding: 0; }
  html, body {
    width: 1200px; height: 901px; overflow: hidden;
    background: var(--page-bg);
    font-family: "Open Sans", Verdana, sans-serif;
    color: var(--ink);
  }
  .site-card {
    position: absolute; left: 127px; top: 88px; width: 949px; height: 730px;
    background: var(--card-bg);
    box-shadow: 0 2px 10px rgba(0,0,0,0.22);
  }
  .stage {
    position: absolute; left: 12px; top: 9px; width: 925px; height: 650px;
    background: var(--stage-bg);
  }
  .stage-art {
    position: absolute; left: 160px; top: 20px; width: 560px; height: 610px;
    background: radial-gradient(ellipse at center, var(--stage-shape) 0%, var(--stage-bg) 70%);
  }
  .access-band {
    position: absolute; left: 0; top: 180px; width: 949px; height: 212px;
  }
  .brand-panel {
    position: absolute; left: 0; top: 0; width: 440px; height: 212px;
    background: var(--logo-panel);
    border-top: 12px solid var(--accent);
    border-bottom: 12px solid var(--accent);
    display: flex; align-items: center; padding-left: 40px; gap: 20px;
  }
  .brand-mark {
    width: 74px; height: 74px; background: var(--accent-dark); flex: none;
  }
  .brand-name {
    color: #e9e9e9; font-weight: 600; font-size: 27px; line-height: 1.15;
    letter-spacing: 1px; text-transform: uppercase;
  }
  .brand-name span { display: block; font-size: 15px; letter-spacing: 2.5px; }
  .login-panel {
    position: absolute; left: 440px; top: 0; width: 509px; height: 212px;
    background: var(--band-tone);
  }
  .login-title {
    position: absolute; left: 54px; top: 30px;
    color: var(--accent); font-size: 17px; font-weight: 400;
  }
  .field-row {
    position: absolute; left: 54px; display: flex; align-items: center;
    font-size: 13px; color: var(--ink);
  }
  .field-row label { width: 78px; }
  .field-row .input {
    width: 122px; height: 20px; background: var(--field); border: 1px solid #e3e0da;
  }
  .row-user { top: 66px; }
  .row-pass { top: 106px; }
  .go-button {
    margin-left: 15px; width: 31px; height: 21px; background: var(--button);
    color: #fff; font-size: 11px; font-weight: 700; border: 0;
    display: flex; align-items: center; justify-content: center;
  }
  .login-divider {
    position: absolute; left: 0; right: 0; top: 153px; height: 1px; background: var(--band-line);
  }
  .forgot {
    position: absolute; left: 54px; top: 163px; font-size: 12px; color: var(--ink);
  }
  .forgot a { color: var(--ink); text-decoration: underline; }
  .contact {
    position: absolute; left: 317px; top: 62px; font-size: 10.5px; line-height: 15px; color: var(--ink);
  }
  .contact strong { font-weight: 700; }
  .enter-site {
    position: absolute; left: 773px; top: 400px; font-size: 28px; color: #55524d;
    text-decoration: none;
  }
  .copyright {
    position: absolute; right: 22px; top: 688px; font-size: 11px; color: var(--ink);
  }
</style>
</head>
<body>
  <main class="site-card">
    <div class="stage">
      <div class="stage-art" role="img" aria-label="Faint large bull silhouette decoration in beige tones"></div>
    </div>

    <section class="access-band">
      <div class="brand-panel">
        <div class="brand-mark"></div>
        <div class="brand-name">Marlowick<span>Investment Partners</span></div>
      </div>

      <div class="login-panel">
        <h2 class="login-title">Client Access</h2>
        <div class="field-row row-user"><label>User Name:</label><div class="input"></div></div>
        <div class="field-row row-pass"><label>Password:</label><div class="input"></div><div class="go-button">GO</div></div>
        <div class="login-divider"></div>
        <p class="forgot">Forgot your password? Reset it <a href="#">here</a>.</p>
        <address class="contact">
          <strong>Marlowick Investment Partners</strong><br>
          US, 12345<br>
          Email: info@mipfundexample.com<br>
          Phone: (123) 456-7890<br>
          Fax: (123) 456-7890
        </address>
      </div>
    </section>

    <a class="enter-site" href="#">Enter Site</a>
    <p class="copyright">Copyright © 2011 Marlowick Investment Partners</p>
  </main>
</body>
</html>
```